App Design for quiz app (casual gaming app)

We need an design & logo for our quiz app. Its a simple quiz app, where you pick up a category, answer three questions out of this category. After this an opponent is assigned to your game, and has to answer the same three questions. After this first round is finished, it's the opponents turn to choose a new category and answer three questions out of this category. Now it's your turn to answer the same three questions. With this done, the 2nd round is finished. One game has seven rounds.
Please find attached the balsamiq project. For all of you, do not have balsamiq, please find also the mockups as pdf.
Final delivery should be psd files
Target Market(s)
Casual Games

```html
<!DOCTYPE html>
<html lang="en">
<head>
<meta charset="utf-8">
<title>Querivo – Login</title>
<link rel="stylesheet" href="https://fonts.googleapis.com/css2?family=Open+Sans:wght@400;600;700&family=Roboto:wght@300;400&display=swap">
<style>
  :root {
    --bg-top: #46515b;
    --bg-bottom: #3c454e;
    --bg-shape: #4b5660;
    --text: #ffffff;
    --placeholder: #6f7984;
    --rule: #9aa0a6;
    --green: #43a047;
    --blue: #3a82c8;
    --accent: #f5c342;
  }
  * { box-sizing: border-box; margin: 0; padding: 0; }
  html, body { width: 674px; height: 1200px; overflow: hidden; }
  body { font-family: "Open Sans", sans-serif; color: var(--text); background: var(--bg-bottom); }
  .screen { position: relative; width: 674px; height: 1200px; overflow: hidden; }
  .backdrop {
    position: absolute; inset: 0;
    background: linear-gradient(160deg, var(--bg-top) 0%, var(--bg-shape) 45%, var(--bg-bottom) 100%);
  }
  .status-bar {
    position: absolute; top: 4px; left: 0; width: 100%; height: 30px;
    font-family: "Roboto", sans-serif; font-weight: 300; font-size: 19px;
  }
  .status-bar .carrier { position: absolute; left: 12px; top: 0; display: flex; align-items: center; gap: 6px; }
  .status-bar .time { position: absolute; left: 0; width: 100%; text-align: center; top: 0; }
  .status-bar .battery { position: absolute; right: 10px; top: 0; display: flex; align-items: center; gap: 6px; }
  .page-title { position: absolute; top: 74px; width: 100%; text-align: center; font-size: 21px; font-weight: 600; }
  .brand-mark { position: absolute; left: 287px; top: 160px; width: 100px; height: 100px; border-radius: 50%; background: var(--accent); }
  .brand-name { position: absolute; top: 306px; width: 100%; text-align: center; font-size: 45px; font-weight: 600; padding-left: 6px; }
  .field { position: absolute; left: 61px; width: 551px; height: 56px; border-bottom: 2px solid var(--rule); }
  .field span { position: absolute; left: 29px; bottom: 13px; font-size: 25px; font-weight: 600; color: var(--placeholder); }
  .field--user { top: 422px; }
  .field--pass { top: 536px; }
  .forgot { position: absolute; left: 90px; top: 637px; font-size: 25px; font-weight: 600; }
  .btn {
    position: absolute; left: 109px; width: 457px; height: 88px; border-radius: 44px;
    display: flex; align-items: center; justify-content: center; font-weight: 600;
  }
  .btn--confirm { top: 719px; background: var(--green); font-size: 29px; }
  .btn--social { top: 1012px; background: var(--blue); font-size: 25px; justify-content: flex-start; padding-left: 73px; }
  .btn--social .dot { width: 28px; height: 28px; border-radius: 50%; background: var(--text); margin-right: 18px; }
  .register { position: absolute; top: 838px; width: 100%; text-align: center; font-size: 25px; font-weight: 600; letter-spacing: 0.3px; }
  .register strong { font-weight: 700; }
  .divider { position: absolute; top: 921px; width: 100%; text-align: center; font-size: 23px; font-weight: 600; }
</style>
</head>
<body>
<main class="screen">
  <div class="backdrop" role="img" aria-label="Faint illustration of study desk items: notebook, pencil, USB stick and glasses"></div>

  <div class="status-bar">
    <div class="carrier">
      <svg width="70" height="14" viewBox="0 0 70 14" aria-hidden="true">
        <circle cx="7" cy="7" r="6" fill="#fff"/><circle cx="21" cy="7" r="6" fill="#fff"/>
        <circle cx="35" cy="7" r="5.5" fill="none" stroke="#fff"/><circle cx="49" cy="7" r="5.5" fill="none" stroke="#fff"/>
        <circle cx="63" cy="7" r="5.5" fill="none" stroke="#fff"/>
      </svg>
      <span>NT</span>
      <svg width="22" height="16" viewBox="0 0 22 16" aria-hidden="true">
        <path d="M1 6a14 14 0 0 1 20 0M4.5 9.5a9 9 0 0 1 13 0M8 13a4 4 0 0 1 6 0" fill="none" stroke="#fff" stroke-width="2.2"/>
      </svg>
    </div>
    <div class="time">12:53 pm</div>
    <div class="battery">
      <span>31%</span>
      <svg width="52" height="20" viewBox="0 0 52 20" aria-hidden="true">
        <rect x="1" y="1" width="46" height="18" rx="3" fill="none" stroke="#fff" stroke-width="1.5"/>
        <rect x="3" y="3" width="13" height="14" fill="#fff"/>
        <rect x="48" y="7" width="3" height="6" fill="#fff"/>
      </svg>
    </div>
  </div>

  <h1 class="page-title">Login</h1>
  <div class="brand-mark"></div>
  <div class="brand-name">Querivo</div>

  <div class="field field--user"><span>Username or Email Address</span></div>
  <div class="field field--pass"><span>Password</span></div>
  <div class="forgot">Forgot Password?</div>

  <div class="btn btn--confirm">Confirm</div>
  <p class="register">Don’t have an Account ? <strong>Register here.</strong></p>
  <p class="divider">Or</p>
  <div class="btn btn--social"><span class="dot"></span><span>Login With Chatterly</span></div>
</main>
</body>
</html>
```